I have a logo and need to design the business card and stationery.
Updates

The uploaded logo image named as GREYHAVEN CONSTRUCTION which is to be replaced to GREYHAVEN CONTRACTS. Kindly add below details and submit the designs- Company name- Greyhaven Engineering Contracts LLP Name & Post- Kunal Mehra (Designated Partner) Address- Block No.317, Wing C, Tulsi Trade Plaza, Lokhand Marg, Varun Industrial Park, Goregaon(E), Mumbai - 400 063 Contact- +91 97410 58723 Email- kunalmehra@examplemail.com Website- www.greyhavencontracts.example Contact for Letterhead- +91-22-28145597

Hi Tanvir Rahman, We are liking your Design #41927506. We have suggested some changes which are mentioned in feedback. Kindly revert with it asap to finalize this design.

Colors

Designer to choose colors to be used in the design.

```html
<!DOCTYPE html>
<html lang="en">
<head>
<meta charset="utf-8">
<title>Greyhaven Contracts – Stationery</title>
<link rel="stylesheet" href="https://fonts.googleapis.com/css2?family=Michroma&family=Open+Sans:wght@400;600&display=swap">
<style>
  :root{
    --ink:#3a3a3b;
    --ink-soft:#555657;
    --paper:#ffffff;
    --bg-top:#ededed;
    --bg-mid:#dcdcdc;
    --bg-bottom:#cacbcd;
    --ghost:#eeeeef;
    --text:#4a4a4a;
    --text-muted:#5a5a5a;
    --on-dark:#d8d8d8;
  }
  *{margin:0;padding:0;box-sizing:border-box}
  html,body{width:1200px;height:3092px;overflow:hidden}
  body{position:relative;font-family:"Open Sans",Arial,sans-serif;color:var(--text);background:var(--bg-top)}
  .section{position:absolute;left:0;width:1200px}
  .section--suite{top:0;height:790px;background:var(--bg-top)}
  .section--folder{top:790px;height:850px;background:radial-gradient(ellipse at 50% 20%,#ffffff 0%,var(--bg-mid) 70%)}
  .section--flat{top:1640px;height:1452px;background:var(--bg-bottom)}
  .piece{position:absolute;background:var(--paper);box-shadow:0 4px 10px rgba(0,0,0,.18);overflow:hidden}
  .piece--dark{background:var(--ink)}

  .brand{position:absolute;display:flex;flex-direction:column;align-items:center;font-family:"Michroma",sans-serif;color:var(--ink);line-height:1.25;text-align:center}
  .brand--light{color:var(--paper)}
  .brand--left{align-items:flex-start;text-align:left}
  .brand__square{border:3px solid currentColor;margin-bottom:.45em}
  .brand__name{letter-spacing:.12em;white-space:nowrap}

  .tagline{position:absolute;left:0;right:0;text-align:center;font-family:"Michroma",sans-serif;letter-spacing:.16em;white-space:nowrap}
  .tagline--light{color:var(--paper)}
  .tagline--dark{color:var(--ink)}
  .band{position:absolute;left:0;right:0;background:var(--ink)}
  .ghost{position:absolute;border:26px solid var(--ghost)}
  .small{position:absolute;line-height:1.45}
  .letter__body{position:absolute;left:24px;right:24px;top:88px;font-size:5px;line-height:1.55;color:var(--text-muted)}
  .letter__body p{margin-bottom:6px}
  .contact-list{list-style:none}
  .flap{position:absolute;left:0;top:0;width:100%}
  .address{position:absolute;color:var(--ink-soft);line-height:1.4}
</style>
</head>
<body>

<section class="section section--suite">
  <article class="piece letterhead" style="left:291px;top:98px;width:293px;height:414px">
    <div class="band" style="top:0;height:38px"></div>
    <div class="brand brand--light brand--left" style="left:20px;top:6px;font-size:5px">
      <span class="brand__square" style="width:13px;height:13px;border-width:2px"></span>
      <span class="brand__name">GREYHAVEN</span>
      <span class="brand__name">CONTRACTS</span>
    </div>
    <ul class="small contact-list" style="left:180px;top:6px;color:var(--paper);font-size:3.6px">
      <li>Greyhaven Engineering Contracts LLP</li>
      <li>Block No.317, Wing C, Tulsi Trade Plaza,</li>
      <li>Lokhand Marg, Varun Industrial Park,</li>
      <li>Goregaon(E), Mumbai - 400 063</li>
      <li>+91-22-28145597</li>
      <li>www.greyhavencontracts.example</li>
    </ul>
    <div class="letter__body">
      <p>Dear customer,</p>
      <p>Thank you for choosing us for your project. Our team has reviewed the site plans and prepared a schedule that keeps every stage on time and within budget. We will share weekly progress reports.</p>
      <p>Our engineers inspect all materials before delivery and follow strict safety standards on site. Any change to the scope will be agreed in writing before work begins.</p>
      <p>Please contact our office with any questions. We look forward to building with you.</p>
      <p>Yours Sincerely,</p>
    </div>
    <div class="band" style="bottom:0;height:12px"></div>
    <span class="tagline tagline--light" style="bottom:3px;font-size:4px">CRAFTED FOR ENDURANCE.</span>
  </article>

  <article class="piece piece--dark folder-cover" style="left:637px;top:80px;width:346px;height:437px">
    <div class="brand brand--light" style="left:0;right:0;top:150px;font-size:13px">
      <span class="brand__square" style="width:44px;height:44px;border-width:5px"></span>
      <span class="brand__name">GREYHAVEN</span>
      <span class="brand__name">CONTRACTS</span>
    </div>
    <span class="tagline tagline--light" style="bottom:34px;font-size:6.5px">CRAFTED FOR ENDURANCE.</span>
  </article>

  <article class="piece piece--dark card-front" style="left:186px;top:550px;width:132px;height:50px">
    <div class="brand brand--light" style="left:0;right:0;top:6px;font-size:4.6px">
      <span class="brand__square" style="width:10px;height:10px;border-width:2px"></span>
      <span class="brand__name">GREYHAVEN</span>
      <span class="brand__name">CONTRACTS</span>
    </div>
    <span class="tagline tagline--light" style="bottom:4px;font-size:3.4px">CRAFTED FOR ENDURANCE.</span>
  </article>

  <article class="piece card-back" style="left:186px;top:612px;width:132px;height:46px">
    <div class="small" style="left:6px;top:5px;font-size:3.4px;color:var(--ink)">
      <strong style="font-size:4.4px">KUNAL MEHRA</strong><br>Designated Partner<br><br>
      +91 97410 58723<br>kunalmehra@examplemail.com<br>www.greyhavencontracts.example<br>
      Block No.317, Wing C, Tulsi Trade Plaza, Goregaon(E)
    </div>
    <div class="brand" style="left:86px;top:5px;font-size:3.8px">
      <span class="brand__square" style="width:8px;height:8px;border-width:1.5px"></span>
      <span class="brand__name">GREYHAVEN</span>
      <span class="brand__name">CONTRACTS</span>
    </div>
  </article>

  <article class="piece compliment-slip" style="left:354px;top:550px;width:300px;height:168px">
    <div class="ghost" style="left:186px;top:20px;width:120px;height:120px"></div>
    <div class="brand brand--left" style="left:16px;top:12px;font-size:5px">
      <span class="brand__square" style="width:12px;height:12px;border-width:2px"></span>
      <span class="brand__name">GREYHAVEN</span>
      <span class="brand__name">CONTRACTS</span>
    </div>
    <p class="address" style="left:16px;top:48px;font-size:3.6px">Greyhaven Engineering Contracts LLP<br>Block No.317, Wing C, Tulsi Trade Plaza,<br>Lokhand Marg, Varun Industrial Park,<br>Goregaon(E), Mumbai - 400 063</p>
    <div class="band" style="bottom:0;height:11px"></div>
    <span class="tagline tagline--light" style="bottom:3px;font-size:4px">CRAFTED FOR ENDURANCE.</span>
  </article>

  <article class="piece envelope" style="left:714px;top:557px;width:291px;height:161px">
    <svg class="flap" width="291" height="52" viewBox="0 0 291 52"><polygon points="0,0 291,0 291,40 280,52 11,52 0,40" fill="var(--ink)"/></svg>
    <div class="brand brand--light" style="left:0;right:0;top:14px">
      <span class="brand__square" style="width:16px;height:16px;border-width:3px;margin:0"></span>
    </div>
  </article>
</section>

<section class="section section--folder">
  <article class="piece piece--dark folder-outside" style="left:150px;top:190px;width:450px;height:440px">
    <div class="brand brand--light" style="left:0;right:0;top:110px;font-size:17px">
      <span class="brand__square" style="width:58px;height:58px;border-width:6px"></span>
      <span class="brand__name">GREYHAVEN</span>
      <span class="brand__name">CONTRACTS</span>
    </div>
    <p class="address" style="left:0;right:0;bottom:28px;text-align:center;color:var(--on-dark);font-size:7px">Greyhaven Engineering Contracts LLP<br>Block No.317, Wing C, Tulsi Trade Plaza, Lokhand Marg, Varun Industrial Park, Goregaon(E), Mumbai - 400 063<br>+91-22-28145597 · kunalmehra@examplemail.com · www.greyhavencontracts.example</p>
  </article>
  <article class="piece folder-inside" style="left:600px;top:190px;width:450px;height:440px">
    <div class="brand" style="left:0;right:0;top:110px;font-size:17px">
      <span class="brand__square" style="width:58px;height:58px;border-width:6px"></span>
      <span class="brand__name">GREYHAVEN</span>
      <span class="brand__name">CONTRACTS</span>
    </div>
    <span class="tagline tagline--dark" style="bottom:40px;font-size:8px">CRAFTED FOR ENDURANCE.</span>
  </article>
</section>

<section class="section section--flat">
  <article class="piece letterhead-flat" style="left:143px;top:130px;width:438px;height:708px">
    <div class="ghost" style="left:232px;top:478px;width:230px;height:230px;border-width:40px"></div>
    <div class="brand brand--left" style="left:52px;top:30px;font-size:7px">
      <span class="brand__square" style="width:24px;height:24px;border-width:3px"></span>
      <span class="brand__name">GREYHAVEN</span>
      <span class="brand__name">CONTRACTS</span>
    </div>
    <p class="address" style="left:42px;top:90px;font-size:6px;text-align:center">Greyhaven Engineering Contracts LLP<br>Block No.317, Wing C, Tulsi Trade Plaza,<br>Lokhand Marg, Varun Industrial Park,<br>Goregaon(E), Mumbai - 400 063</p>
  </article>
  <article class="piece envelope-large" style="left:620px;top:130px;width:437px;height:708px">
    <svg class="flap" width="437" height="66" viewBox="0 0 437 66"><polygon points="0,0 437,0 437,42 418,66 19,66 0,42" fill="var(--ink)"/></svg>
    <span class="tagline tagline--light" style="top:26px;font-size:8px">CRAFTED FOR ENDURANCE.</span>
  </article>

  <article class="piece letterhead-medium" style="left:143px;top:886px;width:441px;height:296px">
    <div class="ghost" style="left:262px;top:100px;width:190px;height:190px;border-width:34px"></div>
    <div class="brand brand--left" style="left:52px;top:36px;font-size:6.5px">
      <span class="brand__square" style="width:22px;height:22px;border-width:3px"></span>
      <span class="brand__name">GREYHAVEN</span>
      <span class="brand__name">CONTRACTS</span>
    </div>
    <p class="address" style="left:42px;top:92px;font-size:5.6px;text-align:center">Greyhaven Engineering Contracts LLP<br>Block No.317, Wing C, Tulsi Trade Plaza,<br>Lokhand Marg, Varun Industrial Park,<br>Goregaon(E), Mumbai - 400 063</p>
  </article>
  <article class="piece envelope-medium" style="left:616px;top:886px;width:441px;height:296px">
    <svg class="flap" width="441" height="66" viewBox="0 0 441 66"><polygon points="0,0 441,0 441,42 422,66 19,66 0,42" fill="var(--ink)"/></svg>
    <span class="tagline tagline--light" style="top:26px;font-size:8px">CRAFTED FOR ENDURANCE.</span>
  </article>

  <article class="piece letterhead-small" style="left:143px;top:1232px;width:441px;height:205px">
    <div class="ghost" style="left:240px;top:0;width:180px;height:180px;border-width:32px"></div>
    <div class="brand brand--left" style="left:36px;top:36px;font-size:6px">
      <span class="brand__square" style="width:20px;height:20px;border-width:3px"></span>
      <span class="brand__name">GREYHAVEN</span>
      <span class="brand__name">CONTRACTS</span>
    </div>
    <p class="address" style="left:28px;top:86px;font-size:5.2px;text-align:center">Greyhaven Engineering Contracts LLP<br>Block No.317, Wing C, Tulsi Trade Plaza,<br>Lokhand Marg, Varun Industrial Park,<br>Goregaon(E), Mumbai - 400 063</p>
  </article>
  <article class="piece envelope-small" style="left:616px;top:1232px;width:441px;height:205px">
    <svg class="flap" width="441" height="68" viewBox="0 0 441 68"><polygon points="0,0 441,0 441,44 422,68 19,68 0,44" fill="var(--ink)"/></svg>
    <span class="tagline tagline--light" style="top:26px;font-size:8px">CRAFTED FOR ENDURANCE.</span>
  </article>
</section>

</body>
</html>
```